Tidewell Recovery Business Card Design

Professional and clean design. The design colors should flow with the logo. Two-sided card with the website on the back which is:

www.TidewellRecovery.example.

"Specializing in Water Damage Restoration"

On the front I need the name, email, phone, and logo.

Name: Dorian Vashti
Email: Dorian@TidewellRecovery.example
Phone: 555-318-2046 for now

I only have the Preview and Thumbnail right now but should have the source files uploaded within a day or two.

Target Market(s)

Flood victims, home owners with water damage from busted pipes etc...

Industry/Entity Type

Business

Contact Information for Business Card

Name: Dorian Vashti

Font styles to use
Serif
Sans Serif

```html
<!DOCTYPE html>
<html lang="en">
<head>
<meta charset="utf-8">
<title>Tidewell Recovery Business Card</title>
<link rel="stylesheet" href="https://fonts.googleapis.com/css2?family=Cinzel:wght@500&family=Open+Sans:wght@400;600&display=swap">
<style>
  :root {
    --backdrop: #e9eaec;
    --card: #ffffff;
    --brand-blue: #2b8fd3;
    --deep-blue: #1f86d0;
    --sky-blue: #5cc0ef;
    --pale-blue: #a9dcf5;
    --rule-grey: #b8b8b8;
    --text-grey: #555a5f;
  }
  * { box-sizing: border-box; margin: 0; padding: 0; }
  html, body {
    width: 1200px; height: 1000px; overflow: hidden;
    background: var(--backdrop);
  }
  .canvas { position: relative; width: 1200px; height: 1000px; }
  .card {
    position: absolute; left: 265px; width: 665px; height: 397px;
    background: var(--card); border-radius: 22px; overflow: hidden;
    box-shadow: 0 4px 14px rgba(0,0,0,0.18);
  }
  .card--front { top: 73px; }
  .card--back { top: 533px; }

  .brand {
    position: absolute; display: flex; flex-direction: column; align-items: center;
  }
  .brand__dot {
    width: 80px; height: 80px; border-radius: 50%; background: var(--brand-blue);
  }
  .brand__name {
    font-family: 'Cinzel', serif; font-weight: 500;
    color: var(--brand-blue); letter-spacing: 0.5px; white-space: nowrap;
    text-align: center;
  }
  .card--front .brand { left: 0; top: 30px; width: 342px; }
  .card--front .brand__name { font-size: 25px; margin-top: 26px; }
  .card--back .brand { left: 0; right: 0; top: 63px; }
  .card--back .brand__dot { width: 100px; height: 100px; }
  .card--back .brand__name { font-size: 44px; margin-top: 30px; }

  .rule {
    position: absolute; left: 32px; top: 241px; width: 413px; height: 1.5px;
    background: var(--rule-grey);
  }
  .holder-name {
    position: absolute; left: 457px; top: 228px;
    font-family: 'Open Sans', sans-serif; font-weight: 600; font-size: 20px;
    color: var(--deep-blue);
  }
  .contact-list {
    position: absolute; left: 32px; top: 258px; list-style: none;
    font-family: 'Open Sans', sans-serif; font-size: 16.5px; color: var(--text-grey);
  }
  .contact-list li { display: flex; align-items: center; height: 25px; }
  .contact-list svg { width: 14px; height: 14px; margin-right: 8px; flex: none; }

  .wave { position: absolute; left: 0; bottom: 0; width: 665px; height: 70px; }

  .tagline {
    position: absolute; left: 0; right: 0; top: 347px; text-align: center;
    font-family: 'Open Sans', sans-serif; font-size: 16.5px; color: var(--text-grey);
  }
</style>
</head>
<body>
<div class="canvas">

  <section class="card card--front">
    <div class="brand">
      <div class="brand__dot"></div>
      <div class="brand__name">Tidewell Recovery</div>
    </div>

    <div class="rule"></div>
    <div class="holder-name">Dorian Vashti</div>

    <ul class="contact-list">
      <li>
        <svg viewBox="0 0 14 14"><path fill="var(--deep-blue)" d="M1 5c0-2 2-3 6-3s6 1 6 3l-3 1-1-2H5L4 6zM3 7h8l1 5H2z"/></svg>
        555-318-2046
      </li>
      <li>
        <svg viewBox="0 0 14 14"><rect x="1" y="3" width="12" height="8" fill="var(--deep-blue)"/><path d="M1.5 3.5 7 8l5.5-4.5" stroke="#fff" stroke-width="1.2" fill="none"/></svg>
        Dorian@TidewellRecovery.example
      </li>
      <li>
        <svg viewBox="0 0 14 14"><circle cx="7" cy="7" r="6" fill="var(--deep-blue)"/><path d="M1 7h12M7 1c-3 3-3 9 0 12M7 1c3 3 3 9 0 12" stroke="#fff" stroke-width="0.9" fill="none"/></svg>
        www.TidewellRecovery.example
      </li>
    </ul>

    <svg class="wave" viewBox="0 0 665 80" preserveAspectRatio="none">
      <path d="M0 10 C120 30 260 32 420 14 C520 2 600 -2 665 6 V80 H0Z" fill="var(--deep-blue)"/>
      <path d="M0 22 C140 40 280 44 430 26 C530 14 610 10 665 14 V80 H0Z" fill="#ffffff"/>
      <path d="M0 30 C150 50 300 54 440 34 C540 20 610 18 665 20 V80 H0Z" fill="var(--sky-blue)"/>
      <path d="M60 42 C180 56 300 56 420 40" stroke="var(--pale-blue)" stroke-width="2" fill="none"/>
    </svg>
  </section>

  <section class="card card--back">
    <div class="brand">
      <div class="brand__dot"></div>
      <div class="brand__name">Tidewell Recovery</div>
    </div>
    <p class="tagline">Specializing in Water Damage Restoration</p>
  </section>

</div>
</body>
</html>
```